Website for a start-up named Trx SolumWave.

The company is currently producing a sustainable tactical training measure for soldiers in the defense industry. We’d like a simple website design. As the product hasn’t been launched yet, we will not tell too much about the product and it’s not for sale either. We have a website on wix called trxsolumwave.com which we would like to proceed with. The design just needs a professional and loving touch. We develop an add on for KZ90 rifles.

Target Market(s)

Defense industry

Industry/Entity Type

Defense

Coding

Coded - Design and coding required

Number of Pages Required

1 page

```html
<!DOCTYPE html>
<html lang="en">
<head>
<meta charset="utf-8">
<title>Trx SolumWave</title>
<link href="https://fonts.googleapis.com/css2?family=Audiowide&family=Montserrat:wght@400;500;700&display=swap" rel="stylesheet">
<style>
  :root {
    --ink: #111111;
    --dark: #131313;
    --white: #ffffff;
    --paper: #f7f7f7;
    --text: #222222;
    --muted: #bbbbbb;
    --accent: #1fa59a;
    --display: "Audiowide", sans-serif;
    --body: "Montserrat", sans-serif;
  }
  * { box-sizing: border-box; margin: 0; padding: 0; }
  html, body { width: 1200px; height: 3248px; overflow: hidden; background: var(--white); }
  body { font-family: var(--body); color: var(--text); }
  section, footer { position: relative; width: 1200px; overflow: hidden; }
  .abs { position: absolute; }

  /* Hero */
  .hero { height: 646px; background: linear-gradient(180deg, #3a3530 0%, #4a4238 40%, #3b3a33 70%, #25231f 100%); color: var(--white); }
  .hero-photo { inset: 0; background: radial-gradient(ellipse at 30% 40%, rgba(120,105,85,.45), transparent 60%), radial-gradient(ellipse at 80% 55%, rgba(95,100,80,.4), transparent 55%); }
  .hero-shade { inset: 0; background: rgba(15,12,10,.45); }
  .nav-link { top: 43px; font-size: 15px; color: var(--white); }
  .nav-link.active::after { content: ""; display: block; height: 2px; background: var(--white); margin-top: 6px; }
  .brand { top: 32px; left: 520px; width: 160px; text-align: center; font-family: var(--display); font-size: 19px; color: var(--white); line-height: 1; }
  .brand small { display: block; font-family: var(--body); font-size: 9px; letter-spacing: 7px; margin-top: 7px; }
  .btn-outline { border: 1.5px solid var(--white); border-radius: 6px; color: var(--white); display: flex; align-items: center; justify-content: center; font-size: 14px; }
  .hero-title { top: 282px; width: 100%; text-align: center; font-family: var(--display); font-size: 48px; }
  .hero-text { top: 360px; left: 176px; width: 848px; text-align: center; font-size: 19px; line-height: 28px; }
  .chevron { top: 586px; left: 588px; }

  /* Who we are */
  .about { height: 535px; background: var(--white); }
  .about-photo { left: 154px; top: 96px; width: 368px; height: 370px; background: linear-gradient(135deg, #7c8a6a, #3e4250 45%, #22242c 70%, #5d6650); }
  .heading { font-family: var(--display); font-size: 33px; color: var(--ink); }
  .rule { height: 3px; background: var(--ink); }
  .copy { font-size: 13.5px; line-height: 20.6px; }
  .pill { background: var(--ink); color: var(--white); border-radius: 14px; display: flex; align-items: center; justify-content: center; font-size: 11px; font-weight: 500; }

  /* Technology */
  .tech { height: 547px; background: var(--dark); color: var(--white); }
  .tech-photo { left: 631px; top: 0; width: 569px; height: 547px; background: linear-gradient(90deg, var(--dark) 0%, #1d2c3a 20%, #3c6a88 50%, #23384a 75%, #101820 100%); }
  .tech .heading { color: var(--white); text-transform: uppercase; line-height: 45px; }
  .tech .rule { background: var(--white); }
  .btn-ghost { border: 1.5px solid var(--white); border-radius: 14px; color: var(--white); display: flex; align-items: center; justify-content: center; font-size: 11px; }

  /* Services */
  .services { height: 664px; background: var(--paper); }
  .card { top: 209px; width: 290px; height: 360px; background: var(--white); border-radius: 4px; box-shadow: 0 2px 10px rgba(0,0,0,.05); text-align: center; }
  .card-photo { position: absolute; left: 0; top: 0; width: 290px; height: 152px; border-radius: 4px 4px 0 0; }
  .card-icon { position: absolute; left: 122px; top: 129px; width: 46px; height: 46px; border-radius: 50%; background: var(--white); display: flex; align-items: center; justify-content: center; }
  .card-title { position: absolute; top: 178px; width: 100%; font-family: var(--display); font-size: 17px; text-transform: uppercase; color: var(--ink); }
  .card-rule { position: absolute; top: 203px; left: 110px; width: 70px; height: 2px; background: var(--ink); }
  .card-text { position: absolute; top: 212px; left: 22px; width: 246px; font-size: 9.5px; line-height: 14.6px; }
  .card .pill { position: absolute; top: 328px; left: 111px; width: 68px; height: 18px; font-size: 8px; }

  /* Contact */
  .contact { height: 504px; background: var(--ink); color: var(--white); }
  .contact-photo { left: 0; top: 0; width: 640px; height: 504px; background: linear-gradient(90deg, #2a3340 0%, #3b4552 45%, #1c1f24 80%, var(--ink) 100%); }
  .field { background: var(--white); border-radius: 2px; color: #999; font-size: 12px; padding-left: 18px; display: flex; align-items: center; }

  /* Footer */
  footer { height: 352px; background: var(--ink); color: var(--white); }
  .foot-brand { left: 113px; top: 80px; width: 200px; text-align: center; font-family: var(--display); font-size: 32px; color: var(--accent); line-height: 1; }
  .foot-brand small { display: block; font-family: var(--body); font-size: 10px; letter-spacing: 8px; margin-top: 8px; color: var(--muted); }
  .foot-head { top: 75px; font-size: 17px; font-weight: 700; text-transform: uppercase; }
  .foot-list { list-style: none; font-size: 13px; line-height: 21px; text-transform: uppercase; }
  .foot-contact { list-style: none; font-size: 12px; line-height: 17px; font-weight: 500; }
  .foot-contact li { display: flex; gap: 10px; margin-bottom: 6px; }
  .social { top: 117px; width: 22px; height: 22px; border-radius: 50%; background: var(--white); }
  .foot-rule { left: 172px; top: 285px; width: 854px; height: 1px; background: #444; }
  .copyright { top: 294px; width: 100%; text-align: center; font-size: 11px; }
</style>
</head>
<body>

<section class="hero">
  <div class="abs hero-photo" role="img" aria-label="Soldiers in camouflage with rifles standing in front of rusted industrial machinery"></div>
  <div class="abs hero-shade"></div>
  <a class="abs nav-link active" style="left:245px">Home</a>
  <a class="abs nav-link" style="left:323px">About Us</a>
  <a class="abs nav-link" style="left:422px">Services</a>
  <div class="abs brand">Trx SolumWave<small>DEFENSE</small></div>
  <a class="abs nav-link" style="left:721px">Shop</a>
  <a class="abs nav-link" style="left:795px">Contact Us</a>
  <a class="abs btn-outline" style="left:1016px;top:41px;width:135px;height:28px;font-size:13px">Get Started</a>
  <h1 class="abs hero-title">Trx SolumWave</h1>
  <p class="abs hero-text">Lorem ipsum dolor sit amet, consetetur sadipscing elitr, sed diam nonumy eirmod tempor invidunt ut labore et dolore magna aliquyam erat, sed diam voluptua. At vero eos et accusam et justo duo dolores</p>
  <a class="abs btn-outline" style="left:540px;top:466px;width:120px;height:33px;font-size:16px">Learn More</a>
  <svg class="abs chevron" width="24" height="28" viewBox="0 0 24 28" fill="none" stroke="#fff" stroke-width="2.5"><path d="M5 5l7 7 7-7M5 15l7 7 7-7"/></svg>
</section>

<section class="about">
  <div class="abs about-photo" role="img" aria-label="Soldier in helmet with night-vision goggles aiming a rifle"></div>
  <h2 class="abs heading" style="left:605px;top:120px">Who We Are</h2>
  <div class="abs rule" style="left:609px;top:183px;width:207px"></div>
  <p class="abs copy" style="left:609px;top:198px;width:456px">Lorem ipsum dolor sit amet, consetetur sadipscing elitr, sed diam nonumy eirmod tempor invidunt ut labore et dolore magna aliquyam erat, sed diam voluptua. At vero eos et accusam et justo duo dolores et ea rebum. Stet clita kasd gubergren, no sea takimata sanctus est Lorem ipsum dolor sit amet. Lorem ipsum dolor sit amet, consetetur sadipscing elitr, sed diam nonumy eirmod tempor invidunt ut labore et dolore magna aliquyam erat, sed diam voluptua. At vero eos et accusam et justo duo dolores et ea rebum. Stet clita kasd gubergren, no sea takimata sanctus est Lorem ipsum dolor sit amet.</p>
  <a class="abs pill" style="left:609px;top:416px;width:94px;height:27px">Learn More</a>
</section>

<section class="tech">
  <div class="abs tech-photo" role="img" aria-label="Two soldiers in camouflage working on a laptop in a lit server room corridor"></div>
  <h2 class="abs heading" style="left:83px;top:92px">Our Innovative<br>Technology</h2>
  <div class="abs rule" style="left:83px;top:185px;width:290px"></div>
  <p class="abs copy" style="left:83px;top:222px;width:452px">Lorem ipsum dolor sit amet, consetetur sadipscing elitr, sed diam nonumy eirmod tempor invidunt ut labore et dolore magna aliquyam erat, sed diam voluptua. At vero eos et accusam et justo duo dolores et ea rebum. Stet clita kasd gubergren, no sea takimata sanctus est Lorem ipsum dolor sit amet. Lorem ipsum dolor sit amet, consetetur sadipscing elitr, sed diam nonumy eirmod tempor invidunt ut labore et dolore magna aliquyam erat, sed diam voluptua. At vero eos et accusam et justo duo dolores et ea rebum. Stet clita kasd gubergren, no sea takimata sanctus est Lorem ipsum dolor sit amet.</p>
  <a class="abs btn-ghost" style="left:83px;top:455px;width:95px;height:27px">Learn More</a>
</section>

<section class="services">
  <h2 class="abs heading" style="top:80px;width:100%;text-align:center">Our Services</h2>
  <div class="abs rule" style="left:500px;top:143px;width:199px"></div>

  <article class="abs card" style="left:101px">
    <div class="card-photo" role="img" aria-label="Black and white photo of soldiers aiming rifles" style="background:linear-gradient(180deg,#d8d8d8,#6a6a6a 60%,#2c2c2c)"></div>
    <div class="card-icon"><svg width="30" height="30" viewBox="0 0 30 30" fill="none" stroke="#222" stroke-width="1.6"><circle cx="15" cy="15" r="12"/><circle cx="15" cy="15" r="7"/><circle cx="15" cy="15" r="2.5"/></svg></div>
    <h3 class="card-title">Best Equipment</h3>
    <div class="card-rule"></div>
    <p class="card-text">Lorem ipsum dolor sit amet, consetetur sadipscing elitr, sed diam nonumy eirmod tempor invidunt ut labore et dolore magna aliquyam erat, sed diam voluptua. At vero eos et accusam et justo duo sit amet, consetetur sadipscing elitr, sed diam nonumy eirmod tempor invidunt ut labore et dolore</p>
    <a class="pill">Learn More</a>
  </article>

  <article class="abs card" style="left:449px">
    <div class="card-photo" role="img" aria-label="Soldiers crouching with rifles on dusty ground" style="background:linear-gradient(180deg,#7a6a52,#4e4233 60%,#3a3227)"></div>
    <div class="card-icon"><svg width="30" height="30" viewBox="0 0 30 30" fill="none" stroke="#222" stroke-width="1.5"><rect x="7" y="5" width="16" height="11" rx="1"/><path d="M10 9h10M10 12h10"/><rect x="5" y="19" width="4" height="6"/><rect x="11" y="19" width="4" height="6"/><rect x="17" y="19" width="4" height="6"/><rect x="23" y="19" width="3" height="6"/></svg></div>
    <h3 class="card-title">Tactical Gear</h3>
    <div class="card-rule"></div>
    <p class="card-text">Lorem ipsum dolor sit amet, consetetur sadipscing elitr, sed diam nonumy eirmod tempor invidunt ut labore et dolore magna aliquyam erat, sed diam voluptua. At vero eos et accusam et justo duo sit amet, consetetur sadipscing elitr, sed diam nonumy eirmod tempor invidunt ut labore et</p>
    <a class="pill">Learn More</a>
  </article>

  <article class="abs card" style="left:797px">
    <div class="card-photo" role="img" aria-label="Squad of soldiers advancing through a grassy field" style="background:linear-gradient(180deg,#4d5a3c,#6f7552 55%,#5a5a3e)"></div>
    <div class="card-icon"><svg width="30" height="30" viewBox="0 0 30 30" fill="none" stroke="#222" stroke-width="1.6"><path d="M6 10h16l2-3M8 10v4h6l-2 6M12 14l4 8"/><circle cx="22" cy="18" r="3"/></svg></div>
    <h3 class="card-title">Quality Zones</h3>
    <div class="card-rule"></div>
    <p class="card-text">Lorem ipsum dolor sit amet, consetetur sadipscing elitr, sed diam nonumy eirmod tempor invidunt ut labore et dolore magna aliquyam erat, sed diam voluptua. At vero eos et accusam et justo duo sit amet, consetetur sadipscing elitr, sed diam</p>
    <a class="pill">Learn More</a>
  </article>
</section>

<section class="contact">
  <div class="abs contact-photo" role="img" aria-label="Rifle with scattered cartridges lying on a dark tactical vest"></div>
  <h2 class="abs heading" style="left:636px;top:138px;color:var(--white)">Get In Touch</h2>
  <div class="abs rule" style="left:636px;top:203px;width:217px;background:var(--white)"></div>
  <div class="abs field" style="left:633px;top:245px;width:210px;height:40px">First Name</div>
  <div class="abs field" style="left:633px;top:303px;width:210px;height:40px">Email</div>
  <div class="abs field" style="left:859px;top:242px;width:237px;height:103px" aria-label="Message"></div>
  <a class="abs btn-ghost" style="left:633px;top:366px;width:91px;height:32px;font-size:15px;border-radius:16px">Submit</a>
</section>

<footer>
  <div class="abs foot-brand">Trx SolumWave<small>DEFENSE</small></div>
  <p class="abs" style="left:63px;top:156px;width:316px;text-align:center;font-size:12px;line-height:18px">Lorem ipsum dolor sit amet, consetetur sadipscing elitr, sed diam nonumy eirmod tempor invidunt ut labore et dolore magna aliquyam</p>

  <h4 class="abs foot-head" style="left:496px">Usefull Links</h4>
  <ul class="abs foot-list" style="left:496px;top:116px">
    <li>Home</li><li>About Us</li><li>Services</li><li>Shop</li><li>Contact Us</li>
  </ul>

  <h4 class="abs foot-head" style="left:716px">Contact Us</h4>
  <ul class="abs foot-contact" style="left:716px;top:118px;width:190px">
    <li><svg width="9" height="12" viewBox="0 0 9 12" fill="#fff"><path d="M4.5 0A4.5 4.5 0 0 0 0 4.5C0 8 4.5 12 4.5 12S9 8 9 4.5A4.5 4.5 0 0 0 4.5 0zm0 6.2a1.7 1.7 0 1 1 0-3.4 1.7 1.7 0 0 1 0 3.4z"/></svg><span>48 Harbor Lane, Portview,<br>NY 10099</span></li>
    <li><svg width="10" height="10" viewBox="0 0 10 10" fill="#fff"><path d="M2 0l2 2.5-1.2 1.4a6 6 0 0 0 3.3 3.3L7.5 6 10 8l-1.5 2C4 10 0 6 0 1.5z"/></svg><span>+44(0)20 4100-2286</span></li>
    <li><svg width="10" height="8" viewBox="0 0 10 8" fill="#fff"><path d="M0 0h10v8H0zM1 1l4 3 4-3"/></svg><span>info@trxsolumwave.com</span></li>
  </ul>

  <h4 class="abs foot-head" style="left:957px">Social Links</h4>
  <span class="abs social" style="left:977px" aria-label="Social profile"></span>
  <span class="abs social" style="left:1015px" aria-label="Social profile"></span>
  <span class="abs social" style="left:1051px" aria-label="Social profile"></span>

  <div class="abs foot-rule"></div>
  <p class="abs copyright">© 2021 Trx SolumWave All Rights Reserved</p>
</footer>

</body>
</html>
```